Need a redesign for our Wordpress Credit report website

Hi, We need someone to redesign our Wordpress credit report website, brightledgerview.co.za. The designer will be responsible for the following pages:
- home page
- blog page
- single post
- dashboard
- credit report page

About BrightLedgerView.co.za
Bright Ledger View is a consumer focussed credit report platform where South African citizens can get an easy to understand credit report that shows them where to improve their credit scores.

```html
<!DOCTYPE html>
<html lang="en">
<head>
<meta charset="utf-8">
<title>Bright Ledger View – Check your credit score</title>
<link href="https://fonts.googleapis.com/css2?family=Bebas+Neue&family=PT+Sans:wght@400;700&display=swap" rel="stylesheet">
<style>
:root{
  --blue:#2a76d2;
  --blue-light:#3d9af6;
  --blue-deep:#1f64bd;
  --heading:#2567c0;
  --green:#8cc63f;
  --pale:#eef5fd;
  --grey-box:#e9e9ea;
  --text:#222;
  --muted:#444;
  --white:#fff;
}
*{box-sizing:border-box;margin:0;padding:0}
html,body{width:1200px;height:3978px;overflow:hidden}
body{position:relative;background:var(--white);font-family:"PT Sans",sans-serif;color:var(--text)}
.abs{position:absolute}
.display{font-family:"Bebas Neue",sans-serif;color:var(--heading);letter-spacing:1px}
.section-title{left:0;width:1200px;text-align:center;font-size:50px;line-height:1}
.btn{background:var(--green);color:var(--white);font-weight:700;border-radius:20px;text-align:center}

/* header / hero */
.hero-bg{left:0;top:0}
.brand{display:flex;align-items:center;gap:10px;color:var(--white);font-size:22px;font-weight:700}
.brand-dot{width:34px;height:34px;border-radius:50%;background:var(--white)}
.nav{top:36px;left:606px;display:flex;align-items:center;font-size:17px;color:var(--white)}
.nav a{color:var(--white);text-decoration:none;margin-right:44px}
.nav .active{background:var(--white);color:var(--heading);font-weight:700;padding:2px 11px;border-radius:4px;margin-right:34px}
.nav .login{background:var(--green);padding:7px 30px;border-radius:20px;font-weight:700;margin-right:0}
.hero-title{left:0;width:1200px;top:150px;text-align:center;font-size:52px;line-height:48px;color:var(--white)}
.hero-btn{left:530px;top:278px;width:139px;height:35px;line-height:35px;font-size:17px}
.device-art{left:378px;top:367px;width:448px;height:374px;border-radius:14px;background:linear-gradient(180deg,#2b2b2f 0%,#4a4c52 70%,#d7d9dd 100%)}

/* benefits */
.benefit-shape{left:571px;top:795px;width:629px;height:366px;background:var(--pale);border-radius:200px 0 0 200px}
.check-list{list-style:none;font-size:21px}
.check-list li{display:flex;align-items:center;height:40px}
.check-list svg{width:20px;height:12px;margin-right:10px;flex:none}
.benefit-list{left:147px;top:872px}
.screen-card{left:673px;top:846px;width:380px;height:263px;background:var(--white);box-shadow:0 2px 10px rgba(0,0,0,.15)}
.screen-bar{height:14px;background:var(--blue-deep)}
.screen-art{margin:40px 30px 0;height:195px;background:linear-gradient(135deg,#f4f6f9,#dfe7f1)}

/* features */
.feature-shape{left:0;top:1309px;width:641px;height:365px;background:var(--pale);border-radius:0 200px 200px 0}
.feature-photo{left:144px;top:1363px;width:383px;height:254px;border-radius:14px;background:linear-gradient(135deg,#3b4656,#1c2430 55%,#8a7a6c)}
.feature-list{left:670px;top:1343px}

/* testimonial */
.band{left:0;top:1833px;width:1200px;height:495px;background:linear-gradient(90deg,var(--blue-deep) 50%,var(--green) 50%)}
.testi-card{left:145px;top:1916px;width:913px;height:331px;border:3px solid var(--white);border-radius:10px;background:var(--blue-deep)}
.testi-accent{left:365px;top:1950px;width:38px;height:90px;border-radius:19px;background:var(--green)}
.testi-accent2{left:228px;top:2100px;width:42px;height:105px;border-radius:21px;background:var(--white)}
.testi-photo{left:208px;top:1970px;width:210px;height:210px;border-radius:50%;background:linear-gradient(135deg,#e4e8ee,#6c8fc1)}
.stars{left:466px;top:2001px;color:var(--green);font-size:28px;letter-spacing:1px}
.testi-text{left:469px;top:2050px;width:520px;color:var(--white);font-size:16px;line-height:27px}
.dots{left:472px;top:2162px;display:flex;gap:9px}
.dots span{height:5px;width:23px;background:#8fb3e4}
.dots .on{width:77px;background:var(--white)}

/* reviews */
.review{top:2475px;width:287px;height:269px;background:var(--white);box-shadow:0 1px 8px rgba(0,0,0,.12);text-align:center}
.review .quote{position:absolute;left:22px;top:28px;font-family:"Bebas Neue",sans-serif;font-size:90px;line-height:1;color:#c9e4a3}
.review .avatar{position:absolute;left:120px;top:24px;width:46px;height:46px;border-radius:50%;background:linear-gradient(135deg,#b4a08c,#5f4a3a)}
.review .name{position:absolute;top:86px;left:0;width:100%;font-size:27px;line-height:1}
.review .count{position:absolute;top:111px;left:0;width:100%;font-family:"Bebas Neue",sans-serif;font-size:16px;color:#222}
.review p{position:absolute;top:145px;left:16px;right:16px;font-size:16px;line-height:27px;color:var(--muted)}
.view-all{left:550px;top:2784px;width:97px;height:35px;line-height:35px;font-size:16px}

/* why */
.why-box{background:var(--grey-box);padding:26px 15px}
.why-box h3{font-family:"Bebas Neue",sans-serif;color:var(--heading);font-size:22px;font-weight:400;letter-spacing:.5px;margin-bottom:16px}
.why-box p{font-size:13.5px;line-height:22px;color:var(--muted)}

/* footer */
.footer-bg{left:0;top:3180px}
.footer-brand{left:0;width:1200px;top:3530px;justify-content:center;font-size:30px}
.footer-brand .brand-dot{width:44px;height:44px}
.footer-about{left:140px;width:920px;top:3622px;text-align:center;color:var(--white);font-size:16.5px;line-height:27px}
.footer-col{top:3712px;color:var(--white);font-size:14px;line-height:27px}
.footer-col h4{font-size:16px;font-weight:700;line-height:24px}
.pay{width:95px;height:54px;background:var(--white);border-radius:4px;display:flex;align-items:center;justify-content:center;font-size:15px;font-weight:700;color:var(--blue-deep)}
.divider{left:0;top:3883px;width:1200px;height:1px;background:rgba(255,255,255,.35)}
.bottom{top:3908px;color:var(--white);font-size:13px;font-weight:700}
.social{display:inline-flex;gap:12px;margin-left:10px;vertical-align:middle}
.social span{width:14px;height:14px;border-radius:50%;background:var(--white)}
</style>
</head>
<body>

<!-- hero -->
<svg class="abs hero-bg" width="1200" height="620" viewBox="0 0 1200 620" aria-hidden="true">
  <defs><linearGradient id="heroGrad" x1="0" x2="1"><stop offset="0" stop-color="#2a72cf"/><stop offset="1" stop-color="#3d9bf7"/></linearGradient></defs>
  <path d="M0 0H1200V455C1150 540 990 600 780 600H420C210 600 50 540 0 450Z" fill="url(#heroGrad)"/>
</svg>
<div class="abs brand" style="left:144px;top:30px"><span class="brand-dot"></span>Bright Ledger View</div>
<nav class="abs nav">
  <a class="active">Home</a><a>Articles</a><a>About</a><a>Contact</a><a class="login">Login</a>
</nav>
<h1 class="abs display hero-title" style="color:var(--white)">Check your credit score<br>within seconds</h1>
<div class="abs btn hero-btn">Check Score Now</div>
<div class="abs device-art" role="img" aria-label="Desktop and tablet showing an example credit report with a 740 score gauge"></div>

<!-- benefits -->
<div class="abs benefit-shape"></div>
<ul class="abs check-list benefit-list">
  <li><svg viewBox="0 0 20 12"><path d="M2 11A8 8 0 0 1 18 11" fill="none" stroke="#5b8fd6" stroke-width="2"/><path d="M10 11L14 5" stroke="#5b8fd6" stroke-width="2"/></svg>See your most recent credit score</li>
  <li><svg viewBox="0 0 20 12"><path d="M2 11A8 8 0 0 1 18 11" fill="none" stroke="#5b8fd6" stroke-width="2"/><path d="M10 11L14 5" stroke="#5b8fd6" stroke-width="2"/></svg>Get access to your full credit profile</li>
  <li><svg viewBox="0 0 20 12"><path d="M2 11A8 8 0 0 1 18 11" fill="none" stroke="#5b8fd6" stroke-width="2"/><path d="M10 11L14 5" stroke="#5b8fd6" stroke-width="2"/></svg>See who has been looking at your profile</li>
  <li><svg viewBox="0 0 20 12"><path d="M2 11A8 8 0 0 1 18 11" fill="none" stroke="#5b8fd6" stroke-width="2"/><path d="M10 11L14 5" stroke="#5b8fd6" stroke-width="2"/></svg>See if you have any adverse or Blacklistings</li>
</ul>
<div class="abs screen-card">
  <div class="screen-bar"></div>
  <div class="screen-art" role="img" aria-label="Illustration of a person pushing a credit score gauge from poor towards excellent"></div>
</div>

<!-- features -->
<h2 class="abs display section-title" style="top:1220px">System Features</h2>
<div class="abs feature-shape"></div>
<div class="abs feature-photo" role="img" aria-label="Photo of hands typing on a laptop displaying a credit score dashboard"></div>
<ul class="abs check-list feature-list">
  <li><svg viewBox="0 0 20 12"><path d="M2 11A8 8 0 0 1 18 11" fill="none" stroke="#5b8fd6" stroke-width="2"/><path d="M10 11L14 5" stroke="#5b8fd6" stroke-width="2"/></svg>Dispute generator - easily manage disputes</li>
  <li><svg viewBox="0 0 20 12"><path d="M2 11A8 8 0 0 1 18 11" fill="none" stroke="#5b8fd6" stroke-width="2"/><path d="M10 11L14 5" stroke="#5b8fd6" stroke-width="2"/></svg>Budget tool - easily create a budget</li>
  <li><svg viewBox="0 0 20 12"><path d="M2 11A8 8 0 0 1 18 11" fill="none" stroke="#5b8fd6" stroke-width="2"/><path d="M10 11L14 5" stroke="#5b8fd6" stroke-width="2"/></svg>Improve your credit score eBook</li>
  <li><svg viewBox="0 0 20 12"><path d="M2 11A8 8 0 0 1 18 11" fill="none" stroke="#5b8fd6" stroke-width="2"/><path d="M10 11L14 5" stroke="#5b8fd6" stroke-width="2"/></svg>Personal Budgeting Spreadsheet</li>
  <li><svg viewBox="0 0 20 12"><path d="M2 11A8 8 0 0 1 18 11" fill="none" stroke="#5b8fd6" stroke-width="2"/><path d="M10 11L14 5" stroke="#5b8fd6" stroke-width="2"/></svg>Perfect score video course</li>
  <li><svg viewBox="0 0 20 12"><path d="M2 11A8 8 0 0 1 18 11" fill="none" stroke="#5b8fd6" stroke-width="2"/><path d="M10 11L14 5" stroke="#5b8fd6" stroke-width="2"/></svg>Personal Finance Video Tutorials</li>
  <li><svg viewBox="0 0 20 12"><path d="M2 11A8 8 0 0 1 18 11" fill="none" stroke="#5b8fd6" stroke-width="2"/><path d="M10 11L14 5" stroke="#5b8fd6" stroke-width="2"/></svg>Dedicated 24/7 Support</li>
</ul>

<!-- testimonial -->
<h2 class="abs display section-title" style="top:1740px">User Testimonail</h2>
<div class="abs band"></div>
<div class="abs testi-card"></div>
<div class="abs testi-accent"></div>
<div class="abs testi-accent2"></div>
<div class="abs testi-photo" role="img" aria-label="Photo of a smiling family of four"></div>
<div class="abs stars">★★★★★</div>
<p class="abs testi-text">The report was accurate and gave me a good understanding of my current credit status. I found it interesting the way the scoring worked and really enjoyed reading it...guess because I am doing well with managing credit.</p>
<div class="abs dots"><span class="on"></span><span></span><span></span><span></span><span></span></div>

<!-- reviews -->
<h2 class="abs display section-title" style="top:2392px">Customer Reviews</h2>
<div class="abs review" style="left:147px">
  <span class="quote">“</span><span class="avatar" role="img" aria-label="Reviewer profile photo"></span>
  <div class="name display">Marlene Vosloo</div><div class="count">28 Reviews</div>
  <p>The credit report is easy to use, informative and accurate to the date. Helps me to manage my financial well-being.</p>
</div>
<div class="abs review" style="left:459px">
  <span class="quote">“</span><span class="avatar" role="img" aria-label="Reviewer profile photo"></span>
  <div class="name display">Carla Steyn</div><div class="count">2 Reviews</div>
  <p>Their customer support team has been very impressive. The tools and knowledge they shared were of great practical use.</p>
</div>
<div class="abs review" style="left:769px">
  <span class="quote">“</span><span class="avatar" role="img" aria-label="Reviewer profile photo"></span>
  <div class="name display">Ironpeak Fitness ZA</div><div class="count">2 Reviews</div>
  <p>Excellent credit report service. They respond to queries promptly, and have a very detailed credit report which is helpful and informative.</p>
</div>
<div class="abs btn view-all">View All</div>

<!-- why -->
<h2 class="abs display section-title" style="top:2900px">Why get your score from us?</h2>
<div class="abs why-box" style="left:144px;top:2969px;width:447px;height:199px">
  <h3>We don't abuse your personal information:</h3>
  <p>Companies that give out free credit scores use your personal information to sell you financial products. That's how they can afford to give it to you for free. We believe that your personal information should be protected and not abused. That's why we ask a small fee. It enables us to protect your information and not abuse it.</p>
</div>
<div class="abs why-box" style="left:607px;top:2969px;width:448px;height:199px">
  <h3>Our report is super easy to understand:</h3>
  <p>Our credit report is one of the easiest reports to understand. The report is clearly laid out and you will see immediately if you can apply for finance, if you are blacklisted, and where you can improve.</p>
</div>

<!-- footer -->
<svg class="abs footer-bg" width="1200" height="798" viewBox="0 0 1200 798" aria-hidden="true">
  <path d="M0 30C60 150 200 255 420 262H780C1000 255 1140 150 1200 30V798H0Z" fill="var(--blue-deep)"/>
</svg>
<div class="abs why-box" style="left:377px;top:3185px;width:446px;height:178px">
  <h3>300,000 + South Africans have trusted us:</h3>
  <p>Since 2008 we have helped over 300,000 South Africans make sense of their credit reports, so you can rest assured knowing that we have a proven track record and that you are in safe hands with us.</p>
</div>
<div class="abs brand footer-brand" style="display:flex"><span class="brand-dot"></span>Bright Ledger View</div>
<p class="abs footer-about">brightledgerview.co.za (BLV) is a web based platform that enables credit active consumers to get direct access to their credit scores and profiles in an easy to understand and interactive online report.</p>
<div class="abs footer-col" style="left:171px"><h4>TERMS</h4>GENERAL TERMS OF USE<br>EXCLUSION OF LIABILITY<br>SECURITY POLICY<br>PRIVACY POLICY</div>
<div class="abs footer-col" style="left:409px"><h4>PURCHASE</h4>DELIVERY POLICY<br>DATA POLICY<br>REFUND POLICY<br>CHARGES AND FEES</div>
<div class="abs footer-col" style="left:618px"><h4>QUICK LINKS</h4>ABOUT US<br>ARTICLES<br>CONTACT US<br>LOGIN</div>
<div class="abs pay" style="left:804px;top:3710px">Paycard</div>
<div class="abs pay" style="left:925px;top:3710px">Debitline</div>
<div class="abs pay" style="left:804px;top:3787px">Walletpay</div>
<div class="abs pay" style="left:925px;top:3787px">Swiftcard</div>
<div class="abs divider"></div>
<div class="abs bottom" style="left:145px">© copyrights 2022 Bright Ledger View | All Rights Reserved</div>
<div class="abs bottom" style="left:860px;font-size:15px">Follow us : <span class="social"><span></span><span></span><span></span><span></span></span></div>
<div class="abs bottom" style="left:1148px;font-weight:400;font-size:11px">C54</div>

</body>
</html>
```